National Virtual CPA Firm needs post card design

Virtual CPA firm called "QUINDRA" needs a 5.5” x 8.5” post card designed to market our services to middle market mid-size american businesses. We provide Full Service Payroll (includes the processing of payroll, printing of checks and direct depositing, tax filing, and tax payments), Bookkeeping (Using their native systems, or ours), Contract CFO (with expense reduction analysis), Reporting services for business directors to make informed decisions, Capital Fundraising (Advice on seeking equity to help grow your business), and Taxes (Personal (1040), Partnership (1065), Corporate (1120, 1120S (Including Consolidated Returns)), Trust (1041) and Non-Profit (990)), including all affiliated state returns. One of our major selling points is our variety of experience, and our fast turn around times on projects.
This project specifically, I would like to highlight the bookkeeping services, but still want the tax and payroll services listed on the postcard.
I have uploaded the logo design for QUINDRA and would like a postcard that compliments the logo.
Company contact info is:
Quindra accounting services Inc
P.O. Box 4586
Great falls, MT 59471
(800) 362-9174
Www.quindra-example.com
Target Market(s)
Small to medium size businesses
Industry/Entity Type
Accounting

```html
<!DOCTYPE html>
<html lang="en">
<head>
<meta charset="utf-8">
<title>Quindra Postcard</title>
<link href="https://fonts.googleapis.com/css2?family=Fira+Sans+Extra+Condensed:wght@300;400;500;600;700;800&family=Inter:wght@400;500;600;700&display=swap" rel="stylesheet">
<style>
  :root {
    --stage: #acacac;
    --white: #ffffff;
    --paper: #f7f7f7;
    --yellow: #fdcb0b;
    --yellow-soft: #fed85a;
    --green: #1b7d32;
    --green-dark: #0a7138;
    --green-light: #5ab947;
    --ink: #111111;
    --grey-text: #4a4a4a;
    --red: #e31e24;
  }
  * { margin: 0; padding: 0; box-sizing: border-box; }
  html, body { width: 962px; height: 1200px; overflow: hidden; }
  body { background: var(--stage); position: relative; font-family: "Inter", sans-serif; }

  .card { position: absolute; left: 145px; width: 680px; height: 440px; overflow: hidden; background: var(--white); }
  .card--front { top: 126px; }
  .card--back { top: 618px; height: 438px; }

  .front-art { position: absolute; left: 0; top: 0; width: 680px; height: 380px; }

  .front-tagline { position: absolute; right: 76px; top: 208px; text-align: right; font-family: "Fira Sans Extra Condensed", sans-serif; color: var(--grey-text); white-space: nowrap; }
  .front-tagline__main { font-size: 21px; font-weight: 600; line-height: 27px; }
  .front-tagline__sub { font-size: 21px; font-weight: 300; line-height: 27px; }

  .brand-name { position: absolute; font-family: "Fira Sans Extra Condensed", sans-serif; font-weight: 800; color: var(--ink); letter-spacing: 2px; line-height: 1; white-space: nowrap; }
  .front-brand { right: 74px; top: 272px; font-size: 64px; }
  .front-brand__dot { position: absolute; left: 338px; top: 288px; width: 36px; height: 36px; border-radius: 50%; background: var(--yellow); }

  .services-band { position: absolute; left: 0; top: 380px; width: 680px; height: 60px; background: var(--green); border-top: 4px solid var(--green-light); display: flex; justify-content: center; align-items: center; gap: 8px; font-family: "Fira Sans Extra Condensed", sans-serif; font-weight: 500; font-size: 19px; color: var(--white); white-space: nowrap; }
  .services-band .sep { width: 2px; height: 22px; background: var(--yellow); flex: none; }

  .back-panel { position: absolute; left: 381px; top: 0; width: 299px; height: 386px; }
  .stamp-box { position: absolute; left: 575px; top: 33px; width: 78px; height: 90px; border: 1px solid var(--ink); }
  .address-line { position: absolute; left: 423px; width: 229px; height: 1px; background: var(--ink); }
  .back-web { position: absolute; right: 26px; top: 345px; font-size: 14px; color: var(--ink); }

  .back-brand { left: 109px; top: 42px; font-size: 42px; }
  .back-brand__dot { position: absolute; left: 82px; top: 54px; width: 18px; height: 18px; border-radius: 50%; background: var(--yellow); }
  .back-title { position: absolute; left: 39px; top: 110px; font-family: "Fira Sans Extra Condensed", sans-serif; font-weight: 600; font-size: 28px; line-height: 32px; letter-spacing: -0.3px; color: var(--green-dark); white-space: nowrap; }
  .back-title span { color: var(--grey-text); }
  .back-lead { position: absolute; left: 39px; top: 149px; font-size: 15px; line-height: 19.5px; color: var(--ink); letter-spacing: -0.3px; white-space: nowrap; }
  .back-body { position: absolute; left: 41px; top: 202px; width: 290px; font-size: 10.5px; line-height: 13.3px; color: var(--grey-text); letter-spacing: -0.2px; }
  .back-cta { position: absolute; left: 39px; top: 280px; font-size: 12px; line-height: 15px; color: var(--ink); letter-spacing: -0.2px; }
  .back-cta strong { font-weight: 700; }
  .phone-box { position: absolute; left: 40px; top: 317px; width: 210px; height: 39px; background: var(--green-dark); display: flex; align-items: center; }
  .phone-box__icon { width: 40px; height: 39px; background: var(--red); display: flex; align-items: center; justify-content: center; }
  .phone-box__number { color: var(--white); font-weight: 700; font-size: 21px; padding-left: 7px; letter-spacing: -0.2px; white-space: nowrap; }
  .back-address { position: absolute; left: 39px; top: 366px; font-size: 11.5px; color: var(--ink); letter-spacing: -0.2px; }

  .footer-band { position: absolute; left: 0; top: 386px; width: 680px; height: 52px; background: var(--green); color: var(--white); font-size: 11.5px; line-height: 14.5px; text-align: center; padding-top: 10px; letter-spacing: -0.2px; }
</style>
</head>
<body>

<section class="card card--front">
  <svg class="front-art" viewBox="0 0 680 380" width="680" height="380">
    <defs>
      <linearGradient id="sky" x1="0" y1="0" x2="0" y2="1">
        <stop offset="0" stop-color="#2a6fc4"/>
        <stop offset="0.5" stop-color="#cfe3b0"/>
        <stop offset="1" stop-color="#5c9b2c"/>
      </linearGradient>
      <linearGradient id="office" x1="0" y1="0" x2="1" y2="1">
        <stop offset="0" stop-color="#3a3a3a"/>
        <stop offset="1" stop-color="#bdbdbd"/>
      </linearGradient>
    </defs>
    <rect width="680" height="380" fill="var(--paper)"/>
    <path d="M0 0 H680 V85 C560 150 420 180 330 200 C300 220 250 250 180 290 C110 285 50 290 0 306 Z" fill="var(--yellow)"/>
    <path role="img" aria-label="Photo of blue sky over a sunlit green field" d="M0 0 H140 C110 60 80 110 0 270 Z" fill="url(#sky)"/>
    <path role="img" aria-label="Black and white photo of business people reviewing charts on a tablet" d="M424 0 H680 V45 C600 80 520 100 420 90 C400 80 390 70 384 60 Z" fill="url(#office)"/>
  </svg>

  <div class="front-tagline">
    <div class="front-tagline__main">Full-Service Accounting Solutions</div>
    <div class="front-tagline__sub">for Mid-Size Businesses</div>
  </div>

  <div class="front-brand__dot"></div>
  <div class="brand-name front-brand">QUINDRA</div>

  <div class="services-band">
    <span>Bookkeeping</span><span class="sep"></span>
    <span>Payroll</span><span class="sep"></span>
    <span>Contract CFO</span><span class="sep"></span>
    <span>Reporting Services</span><span class="sep"></span>
    <span>Capital Fundraising</span><span class="sep"></span>
    <span>Taxes</span>
  </div>
</section>

<section class="card card--back">
  <svg class="back-panel" viewBox="0 0 299 386" width="299" height="386">
    <rect width="299" height="386" fill="var(--yellow)"/>
    <path d="M0 89 L299 52 V386 L0 344 Z" fill="var(--yellow-soft)"/>
  </svg>
  <div class="stamp-box"></div>
  <div class="address-line" style="top:189px"></div>
  <div class="address-line" style="top:228px"></div>
  <div class="address-line" style="top:268px"></div>
  <div class="address-line" style="top:307px"></div>
  <div class="back-web">www.quindra-example.com</div>

  <div class="back-brand__dot"></div>
  <div class="brand-name back-brand">QUINDRA</div>
  <div class="back-title"><span>QUINDRA</span> Accounting Services Inc.</div>
  <div class="back-lead">Your trusted accounting partner for<br>middle-market, mid-size American businesses</div>
  <p class="back-body">At QUINDRA, we provide full-service payroll, bookkeeping, contract CFO, reporting services, capital fundraising, and tax services to help your business grow. With our expertise and fast turnaround times, we are committed to providing exceptional services tailored to your unique needs.</p>
  <div class="back-cta"><strong>Contact us today to learn more</strong><br>about how we can help your business succeed.</div>
  <div class="phone-box">
    <div class="phone-box__icon">
      <svg width="24" height="24" viewBox="0 0 24 24" role="img" aria-label="Phone">
        <path d="M6.5 2.5 L9.5 7 L7.6 9 C8.8 11.8 11.2 14.2 14 15.4 L16 13.5 L20.5 16.5 L18.8 20.3 C11 20 4 13 3.7 5.2 Z" fill="var(--white)"/>
        <path d="M14 3.5 A6.5 6.5 0 0 1 20.5 10 M14 6.5 A3.5 3.5 0 0 1 17.5 10" stroke="var(--white)" stroke-width="1.5" fill="none"/>
      </svg>
    </div>
    <div class="phone-box__number">(800) 362-9174</div>
  </div>
  <div class="back-address">P.O. Box 4586, Great Falls, MT 59471</div>

  <div class="footer-band">*All affiliated state returns included. Personal (1040), Partnership (1065), Corporate (1120, 1120S<br>(Including Consolidated Returns)), Trust (1041), and Non-Profit (990)</div>
</section>

</body>
</html>
```